Bruntel general construction

We need an website that are similar to these websites:
https://www.morvexa.com/en/
https://dulnari.com/company/

but with a tweak. Do not copy the entire website but atleast similar and yet better than them.

For reference this our current website.
https://bruntel.ph/

For the winning Designer please help us with the migration from our old website to the new redesign website.

```html
<!DOCTYPE html>
<html lang="en">
<head>
<meta charset="utf-8">
<title>Bruntel — Building Tomorrow Together</title>
<link rel="stylesheet" href="https://fonts.googleapis.com/css2?family=Montserrat:ital,wght@1,800;1,900&family=Plus+Jakarta+Sans:wght@400;500;600;700;800&display=swap">
<style>
:root{
  --navy:#0c1f5c;
  --navy-deep:#0a1a4d;
  --blue:#123fa8;
  --orange:#f7871f;
  --ink:#0d1b4a;
  --muted:#5a6378;
  --line:#e4e7ee;
  --white:#ffffff;
  --black:#050608;
}
*{box-sizing:border-box;margin:0;padding:0}
html,body{width:1200px;height:1200px;overflow:hidden;background:#fff}
body{position:relative;font-family:"Plus Jakarta Sans",sans-serif;color:var(--ink)}
.page{position:absolute;left:470px;top:10px;width:1440px;height:7528px;transform:scale(.15625);transform-origin:0 0;background:#fff}
section,footer{position:relative;width:1440px;overflow:hidden}
.label{font-size:20px;font-weight:500;letter-spacing:.5px;text-transform:uppercase;color:var(--ink)}
.label::before{content:"– "}
.h2{font-size:52px;font-weight:800;line-height:64px;text-transform:uppercase;letter-spacing:-1px}
.o{color:var(--orange)}
.dark .label,.dark .h2{color:#fff}
.btn{display:inline-flex;align-items:center;gap:14px;height:52px;padding:0 12px 0 30px;border-radius:26px;background:var(--orange);color:#fff;font-size:17px;font-weight:600}
.btn .dot{width:32px;height:32px;border-radius:50%;background:#fff;opacity:.85}
.abs{position:absolute}

/* hero */
.hero{height:868px;background:linear-gradient(100deg,#1a1410 0%,#3b2414 35%,#8a4a1c 55%,#2a1a16 80%,#120e10 100%)}
.hero .photo{position:absolute;inset:0;background:radial-gradient(ellipse at 75% 55%,rgba(232,96,26,.55),transparent 55%),radial-gradient(ellipse at 30% 20%,rgba(240,130,40,.35),transparent 50%),linear-gradient(180deg,rgba(10,16,40,.5),rgba(0,0,0,.55))}
.nav{position:absolute;top:50px;left:56px;right:40px;display:flex;align-items:center;height:44px}
.brand{display:flex;align-items:center;gap:10px;color:#fff;font-size:22px;font-weight:700}
.brand i{width:22px;height:22px;border-radius:50%;background:var(--orange)}
.menu{display:flex;gap:40px;margin-left:120px;color:#fff;font-size:15px;font-weight:500;text-transform:uppercase}
.nav .cta{margin-left:auto;height:40px;padding:0 40px;border-radius:20px;background:var(--orange);color:#fff;font-size:14px;font-weight:700;display:flex;align-items:center}
.social{display:flex;gap:14px;margin-left:70px}
.social i{width:12px;height:12px;border-radius:50%;background:#fff}
.tags{top:180px;left:56px;color:#fff;font-size:13px;font-weight:700;letter-spacing:1px}
.hero h1{position:absolute;top:236px;left:56px;font-family:"Montserrat",sans-serif;font-style:italic;font-weight:900;font-size:92px;line-height:102px;color:#fff;letter-spacing:-1px}
.hero p{top:588px;left:60px;width:480px;font-size:16px;line-height:22px;color:#f2e6dc}
.hero .btns{top:704px;left:56px;display:flex;gap:36px}
.ghost{display:inline-flex;align-items:center;height:52px;padding:0 32px;border:2px solid rgba(255,255,255,.5);border-radius:26px;color:#fff;font-size:17px}

/* capabilities */
.cap{height:716px}
.cap .label{position:absolute;top:196px;left:56px}
.cap .h2{position:absolute;top:296px;left:56px}
.cap p{position:absolute;top:578px;left:56px;width:540px;font-size:19px;line-height:26px;color:var(--ink)}
.cap-grid{position:absolute;left:776px;top:300px;display:grid;grid-template-columns:repeat(4,150px);row-gap:104px}
.cap-item{text-align:center;font-size:14px;line-height:17px;color:var(--ink);width:110px}
.cap-item svg{display:block;margin:0 auto 16px;width:42px;height:42px}

/* industries */
.ind{height:744px;background:var(--navy)}
.ind .label{position:absolute;top:114px;left:56px}
.ind .h2{position:absolute;top:200px;left:56px}
.row{position:absolute;left:56px;display:flex;gap:76px}
.ind .row{top:392px}
.shot{width:276px;height:276px;border-radius:18px;background:linear-gradient(160deg,#2b78d8,#6a98c4 45%,#c99a2a 70%,#27406e)}
.shot.b{background:linear-gradient(160deg,#343a4a,#c07a40 45%,#e2d2bc 70%,#2a2c36)}
.shot.c{background:linear-gradient(180deg,#5c94dc,#a7b6c8 55%,#4a5260)}
.shot.d{background:linear-gradient(160deg,#1f5fbf,#3f86d8 40%,#1e8a8f 70%,#16325e)}
.arrow{position:absolute;width:40px;height:40px;border-radius:50%;background:#e9ecf2;display:flex;align-items:center;justify-content:center}

/* why */
.why{height:716px}
.why .label{position:absolute;top:94px;left:56px}
.why .h2{position:absolute;top:192px;left:56px}
.why-row{position:absolute;top:460px;left:56px;display:flex;gap:24px}
.why-card{width:200px;height:240px;border:1px solid var(--line);border-radius:10px;box-shadow:0 6px 18px rgba(12,31,92,.07);text-align:center;padding-top:36px}
.why-card svg{width:36px;height:36px}
.why-card small{display:block;margin:16px 20px 0;font-size:10px;line-height:13px;color:var(--muted)}
.why-card b{display:block;margin-top:30px;font-size:13px;font-weight:600}

/* projects */
.proj{height:904px;background:linear-gradient(180deg,#1142b4 0%,#0e2f86 45%,#0b1e5a 100%)}
.proj .label{position:absolute;top:114px;left:56px}
.proj .h2{position:absolute;top:216px;left:56px}
.proj .btn{position:absolute;top:272px;left:1176px;height:52px;font-size:14px}
.proj .row{top:424px}
.pcard{position:relative;width:276px;height:396px;border-radius:18px;overflow:hidden}
.pcard .shot{width:100%;height:100%;border-radius:0}
.pcard .veil{position:absolute;inset:0;background:linear-gradient(180deg,transparent 40%,rgba(5,12,40,.88))}
.pcard .tag{position:absolute;left:16px;top:220px;padding:4px 10px;border-radius:10px;background:rgba(255,255,255,.22);color:#fff;font-size:10px}
.pcard h3{position:absolute;left:18px;top:268px;color:#fff;font-size:19px;line-height:24px;font-weight:700;text-transform:uppercase}
.pcard span{position:absolute;left:18px;top:344px;color:#fff;font-size:11px;font-weight:600}

/* mission */
.mv{height:868px;text-align:center}
.mv .label{position:absolute;top:86px;left:0;width:100%}
.mv .title{position:absolute;top:124px;width:100%;font-size:40px;font-weight:800;text-transform:uppercase;letter-spacing:-1px}
.mv-col{position:absolute;top:220px;width:592px}
.mv-col h2{font-size:94px;font-weight:800;letter-spacing:-4px;color:#1856b8;line-height:112px}
.mv-col .shot{width:100%;height:288px;border-radius:0;margin-top:20px}
.mv-col p{margin-top:40px;text-align:left;font-size:13px;line-height:27px;color:var(--ink)}

/* global */
.glob{height:720px}
.map{position:absolute;left:56px;top:216px;width:744px;height:456px;background:radial-gradient(ellipse at center,#d3d7de 0%,#eceef2 60%,#fff 90%)}
.glob .label{position:absolute;top:78px;left:836px}
.glob .h2{position:absolute;top:168px;left:836px}
.glob p{position:absolute;top:372px;left:836px;width:470px;font-size:19px;line-height:26px;color:var(--ink)}
.glob .btn{position:absolute;top:468px;left:836px;font-size:17px;height:50px}

/* cta */
.cta-band{height:436px;background:linear-gradient(90deg,#f39228 0%,#f08a2a 45%,#e67f20 100%)}
.cta-band::before{content:"";position:absolute;inset:0;background:radial-gradient(ellipse at 80% 40%,rgba(255,255,255,.12),transparent 50%)}
.cta-band h2{position:absolute;top:96px;left:56px;color:#fff;font-size:52px;line-height:64px;font-weight:800;text-transform:uppercase;letter-spacing:-1px}
.cta-band p{position:absolute;top:322px;left:56px;width:380px;font-size:14px;line-height:18px;color:#ffe2c4}
.cta-band .start{position:absolute;top:90px;left:924px;width:412px;height:72px;border-radius:8px;background:var(--navy);color:#fff;font-size:15px;font-weight:700;display:flex;align-items:center;justify-content:center;gap:12px}
.contact{position:absolute;left:1012px;display:flex;gap:22px;color:#fff}
.contact .ico{width:36px;height:36px;border-radius:50%;background:var(--navy);display:flex;align-items:center;justify-content:center}
.contact small{display:block;font-size:11px;opacity:.8}
.contact b{display:block;font-size:13px;font-weight:700}

/* team */
.team{height:612px}
.team .label{position:absolute;top:118px;left:56px}
.team .h2{position:absolute;top:218px;left:56px}
.team p{position:absolute;top:418px;left:56px;width:580px;font-size:15px;line-height:26px}
.member{position:absolute;top:228px;width:356px;height:320px;border-radius:10px;box-shadow:0 6px 20px rgba(12,31,92,.08);text-align:center;padding-top:20px}
.member .avatar{width:184px;height:184px;border-radius:50%;background:#d4d4d4;margin:0 auto}
.member b{display:block;margin-top:48px;font-size:13px;font-weight:500}
.member small{display:block;margin-top:18px;font-size:11px;color:var(--orange)}

/* newsletter */
.news{height:332px;background:linear-gradient(180deg,#5d87c7 0%,#2e5a9c 55%,#12264f 100%)}
.news::before{content:"";position:absolute;inset:0;background:linear-gradient(90deg,rgba(20,40,80,.35),transparent 40%,transparent 60%,rgba(20,40,80,.35))}
.news h2{position:absolute;top:88px;width:100%;text-align:center;color:#fff;font-size:36px;font-weight:400}
.news form{position:absolute;top:186px;left:420px;display:flex}
.news .field{width:504px;height:60px;background:#fff;font-size:15px;color:#9aa0ad;display:flex;align-items:center;padding-left:40px}
.news .go{width:68px;height:60px;background:var(--orange);display:flex;align-items:center;justify-content:center}

/* footer */
footer{height:608px;background:var(--black);color:#fff}
.f-brand{position:absolute;top:60px;left:56px;font-size:22px;font-weight:700;display:flex;align-items:center;gap:10px}
.f-brand i{width:28px;height:28px;border-radius:50%;background:var(--orange)}
.f-about{position:absolute;top:176px;left:52px;width:400px;font-size:15px;line-height:19px;color:#3d7fe0}
.f-cert{position:absolute;top:336px;left:52px;width:400px;font-size:11px;line-height:15px;color:#cfd3da}
.badges{position:absolute;top:460px;left:56px;display:flex;gap:12px}
.badges i{width:72px;height:48px;background:#fff;border-radius:3px}
.fcol{position:absolute;top:90px}
.fcol h4{font-size:17px;font-weight:700;color:var(--orange);margin-bottom:18px}
.fcol li{list-style:none;font-size:12px;line-height:38px;color:#cfd3da}
.fcol p{font-size:12px;line-height:20px;color:#cfd3da;width:320px}
.f-bottom{position:absolute;top:560px;left:60px;right:70px;display:flex;font-size:12px;color:#cfd3da}
.f-bottom span:first-child{flex:1}
.f-bottom span+span{margin-left:140px}
</style>
</head>
<body>
<main class="page">

  <section class="hero">
    <div class="photo" role="img" aria-label="Engineer in orange safety gear and hard hat looking at a refinery lit at sunset"></div>
    <nav class="nav">
      <div class="brand"><i></i>Bruntel</div>
      <div class="menu"><span>Home</span><span>About Us</span><span>Our Services</span><span>Our Team</span><span>News &amp; Media</span><span>Contact Us</span></div>
      <div class="cta">GET IN TOUCH</div>
      <div class="social"><i></i><i></i><i></i></div>
    </nav>
    <div class="abs tags">ENGINEERING • INNOVATION • EXCELLENCE</div>
    <h1>BUILDING<br><span class="o">TOMORROW.</span><br>TOGETHER.</h1>
    <p class="abs">We Support Onshore And Offshore Clients With A Broad Range Of World-Class Services And Highly Trained Staff, Quality Management Systems And Exceptional Safety.</p>
    <div class="abs btns"><span class="btn">Explore Our Services <i class="dot"></i></span><span class="ghost">View Projects →</span></div>
  </section>

  <section class="cap">
    <div class="label">Our Capabilities</div>
    <h2 class="h2">End-to-End Solutions<br>Built For<br><span class="o">Complex Industries</span></h2>
    <p>From Engineering To Maintenance, We Deliver Safe, Reliable, And Efficient Solutions Tailored To Your Operational Needs.</p>
    <div class="cap-grid">
      <div class="cap-item"><svg viewBox="0 0 24 24" fill="none" stroke="#0d1b4a" stroke-width="1.6"><path d="M3 21V10l5 3V8l5 3V4h4v17z"/></svg>Industrial Services</div>
      <div class="cap-item"><svg viewBox="0 0 24 24" fill="none" stroke="#0d1b4a" stroke-width="1.6"><circle cx="12" cy="8" r="4"/><path d="M4 21c1-4 4-6 8-6s7 2 8 6"/></svg>Asset Integrity</div>
      <div class="cap-item"><svg viewBox="0 0 24 24" fill="none" stroke="#0d1b4a" stroke-width="1.6"><path d="M12 3v9l6 3"/><circle cx="12" cy="12" r="9"/></svg>Shutdown &amp; Turnaround</div>
      <div class="cap-item"><svg viewBox="0 0 24 24" fill="none" stroke="#0d1b4a" stroke-width="1.6"><circle cx="12" cy="12" r="3"/><circle cx="12" cy="12" r="8" stroke-dasharray="3 2"/></svg>Mechanical Works</div>
      <div class="cap-item"><svg viewBox="0 0 24 24" fill="none" stroke="#0d1b4a" stroke-width="1.6"><path d="M5 3v18M19 3v18M5 8h14M5 14h14M5 20h14"/></svg>Scaffolding Solutions</div>
      <div class="cap-item"><svg viewBox="0 0 24 24" fill="none" stroke="#0d1b4a" stroke-width="1.6"><path d="M3 8l9-4 9 4-9 4zM3 12l9 4 9-4M3 16l9 4 9-4"/></svg>Insulation Services</div>
      <div class="cap-item"><svg viewBox="0 0 24 24" fill="none" stroke="#0d1b4a" stroke-width="1.6"><path d="M4 4h14v5H4zM11 9v4h-1v8h2v-8h-1"/></svg>Painting &amp; Coatings</div>
      <div class="cap-item"><svg viewBox="0 0 24 24" fill="none" stroke="#0d1b4a" stroke-width="1.6"><path d="M4 20L20 4M14 4h6v6"/></svg>Rope Access &amp; Specialty Access</div>
    </div>
  </section>

  <section class="ind dark">
    <div class="label">Industries We Serve</div>
    <h2 class="h2">Powering <span class="o">Progress</span><br>Across Industries</h2>
    <div class="row">
      <div class="shot" role="img" aria-label="Offshore oil platform"></div>
      <div class="shot b" role="img" aria-label="Engineer reviewing plans on site"></div>
      <div class="shot c" role="img" aria-label="Refinery columns under blue sky"></div>
      <div class="shot d" role="img" aria-label="Water treatment pipework"></div>
    </div>
    <div class="arrow" style="left:36px;top:510px"></div>
    <div class="arrow" style="left:1364px;top:518px"></div>
  </section>

  <section class="why">
    <div class="label">Why Choose Us</div>
    <h2 class="h2">Commited To <span class="o">Safety.</span><br>Driven To Excellence</h2>
    <div class="why-row">
      <div class="why-card"><svg viewBox="0 0 24 24" fill="none" stroke="#0d1b4a" stroke-width="1.6"><path d="M12 3l8 3v6c0 5-4 8-8 9-4-1-8-4-8-9V6z"/></svg><small>Team Focused On Safety With World-Class Standards</small><b>Safety Experts</b></div>
      <div class="why-card"><svg viewBox="0 0 24 24" fill="none" stroke="#0d1b4a" stroke-width="1.6"><circle cx="12" cy="10" r="6"/><path d="M9 15l-2 6 5-2 5 2-2-6"/></svg><small>Team Focused On Safety With World-Class Standards</small><b>Certified Experts</b></div>
      <div class="why-card"><svg viewBox="0 0 24 24" fill="none" stroke="#0d1b4a" stroke-width="1.6"><path d="M9 18h6M10 21h4M12 3a6 6 0 0 0-3 11v2h6v-2a6 6 0 0 0-3-11z"/></svg><small>Team Focused On Safety With World-Class Standards</small><b>Innovation</b></div>
      <div class="why-card"><svg viewBox="0 0 24 24" fill="none" stroke="#0d1b4a" stroke-width="1.6"><circle cx="12" cy="12" r="9"/><path d="M3 12h18M12 3c3 3 3 15 0 18M12 3c-3 3-3 15 0 18"/></svg><small>Team Focused On Safety With World-Class Standards</small><b>Global Standards</b></div>
      <div class="why-card"><svg viewBox="0 0 24 24" fill="none" stroke="#0d1b4a" stroke-width="1.6"><path d="M12 21V9M12 9c-4 0-6-3-6-6 4 0 6 2 6 6zM12 12c3 0 5-2 5-5-3 0-5 2-5 5z"/></svg><small>Team Focused On Safety With World-Class Standards</small><b>Sustainability</b></div>
      <div class="why-card"><svg viewBox="0 0 24 24" fill="none" stroke="#0d1b4a" stroke-width="1.6"><path d="M4 14v-2a8 8 0 0 1 16 0v2M4 14h3v5H4zM17 14h3v5h-3z"/></svg><small>Team Focused On Safety With World-Class Standards</small><b>24/7 Support</b></div>
    </div>
  </section>

  <section class="proj dark">
    <div class="label">Featured Projects</div>
    <h2 class="h2">Success Built On<br><span class="o">Trust</span> And Delivery</h2>
    <span class="btn">View All Projects <i class="dot"></i></span>
    <div class="row">
      <div class="pcard"><div class="shot" role="img" aria-label="Offshore platform at dusk"></div><div class="veil"></div><em class="tag">Environment</em><h3>Safety Standards<br>To The Environment</h3><span>LEARN MORE →</span></div>
      <div class="pcard"><div class="shot b" role="img" aria-label="Refinery skyline at sunset"></div><div class="veil"></div><em class="tag">Petrochemicals</em><h3>Plant Turnaround<br>&amp; Shutdown</h3><span>LEARN MORE →</span></div>
      <div class="pcard"><div class="shot c" role="img" aria-label="Power plant columns"></div><div class="veil"></div><em class="tag">Power Generation</em><h3>Power Plant<br>Insulation</h3><span>LEARN MORE →</span></div>
      <div class="pcard"><div class="shot d" role="img" aria-label="Water system pipework"></div><div class="veil"></div><em class="tag">Water Treatment</em><h3>Disinfection Of<br>Water Systems</h3><span>LEARN MORE →</span></div>
    </div>
    <div class="arrow" style="left:36px;top:600px"></div>
    <div class="arrow" style="left:1364px;top:580px"></div>
  </section>

  <section class="mv">
    <div class="label">Our Mission &amp; Vision</div>
    <div class="title">Expectations <span class="o">Contributes.</span></div>
    <div class="mv-col" style="left:104px">
      <h2>MISSION</h2>
      <div class="shot" role="img" aria-label="Offshore rig structure in yellow steel"></div>
      <p>To Exceed Our Client's Expectations By Demonstratively Adding Value To Their Business By Delivering World-Class Quality Work, Providing Solutions To Critical Challenges, And Making A Significant Impact On Wider Safety And The Environment.</p>
    </div>
    <div class="mv-col" style="left:736px">
      <h2>VISION</h2>
      <div class="shot c" role="img" aria-label="Refinery towers under a blue sky"></div>
      <p>To Become A World Leader That Actively Contributes To The Global Dialogue On Resources Protection, Management, And Sustainability By Providing World-Class Training And Services That Help With The Positive Growth Of Our Clients And Our People.</p>
    </div>
  </section>

  <section class="glob">
    <div class="map" role="img" aria-label="Dotted world map with office location pins"></div>
    <div class="label">Global Presence</div>
    <h2 class="h2">Wherever You Are,<br><span class="o">We Are There.</span></h2>
    <p>A Strong Global Footprints To Support Your Operations Anywhere In The World.</p>
    <span class="btn">Explore Our Locations <i class="dot"></i></span>
  </section>

  <section class="cta-band">
    <h2>Let's Build Something<br>Extraordinary<br>Together</h2>
    <p>Partner With Bruntel For Safe, Innovative And Cost-Effective Industrial Services.</p>
    <div class="start">START YOUR PROJECT <svg width="16" height="16" viewBox="0 0 24 24" fill="none" stroke="#fff" stroke-width="2"><path d="M4 12h16M14 6l6 6-6 6"/></svg></div>
    <div class="contact" style="top:200px"><div class="ico"><svg width="18" height="18" viewBox="0 0 24 24" fill="#fff"><path d="M6 3l4 4-2 3c1 3 3 5 6 6l3-2 4 4-3 3C10 21 3 14 3 6z"/></svg></div><div><small>Call Us Now</small><b>+63 (0) 2 555 0148</b></div></div>
    <div class="contact" style="top:284px"><div class="ico"><svg width="18" height="18" viewBox="0 0 24 24" fill="none" stroke="#fff" stroke-width="2"><rect x="3" y="5" width="18" height="14"/><path d="M3 6l9 7 9-7"/></svg></div><div><small>Email Us</small><b>info@bruntel.ph</b></div></div>
  </section>

  <section class="team">
    <div class="label">Our Team</div>
    <h2 class="h2">Experts Who Build<br><span class="o">Excellence Together.</span></h2>
    <p>With Over 50 Years Of Combined Industry Experience, Our Senior Management Team Possess The Most Competent Skills And Abilities That Ensure Bruntel's Legacy And Success.</p>
    <div class="arrow" style="left:690px;top:376px;background:none">‹</div>
    <div class="member" style="left:736px"><div class="avatar" role="img" aria-label="Portrait placeholder"></div><b>Marisol Dantes</b><small>Country Manager</small></div>
    <div class="member" style="left:1068px"><div class="avatar" role="img" aria-label="Portrait placeholder"></div><b>Owen Larraga</b><small>Managing Director</small></div>
    <div class="arrow" style="left:1312px;top:366px;background:none">›</div>
  </section>

  <section class="news">
    <h2>Stay Updated With Our Latest News &amp; Insight</h2>
    <form><div class="field">Your Email Address</div><div class="go"><svg width="18" height="18" viewBox="0 0 24 24" fill="none" stroke="#fff" stroke-width="2"><path d="M4 12h16M14 6l6 6-6 6"/></svg></div></form>
  </section>

  <footer>
    <div class="f-brand"><i></i>Bruntel</div>
    <p class="f-about">Delivering Integrated Industrial Services That Optimize Performance, Increase Efficiency, And Support Operational Excellence Across Global Industries.</p>
    <p class="f-cert">Our ISO 9001, 14001 And 45001 Certifications Recognize Our Capabilities To Provide World-Class Service To Our Clients While Ensuring That We Are Always One Step Ahead In The Industry.</p>
    <div class="badges"><i></i><i></i><i></i></div>
    <div class="fcol" style="left:520px"><h4>Quick Links</h4><ul><li>About Us</li><li>Our Services</li><li>Industries</li><li>Projects</li><li>Sustainability</li><li>Careers</li></ul></div>
    <div class="fcol" style="left:768px"><h4>Our Services</h4><ul><li>Industrial</li><li>Asset Integrity</li><li>Shutdown &amp;</li><li>Turnaround</li><li>Scaffolding Solutions</li><li>Insulation Services</li></ul></div>
    <div class="fcol" style="left:1028px"><h4>Head Office</h4><p>12 Harbor Way, Marlo District, Cavite, Philippines 4114<br>+63 (0) 2 555 0148</p><h4 style="margin-top:40px">Satellite Office</h4><p>45 Ridge Road, Tanlay, Batangas City, Philippines 4200<br>+63 (0) 43 555 0162</p></div>
    <div class="f-bottom"><span>Copyright © 2026 Bruntel Engineering Philippines, Inc. All Rights Reserved</span><span>Privacy Policy</span><span>Terms Of Use</span><span>Sitemap</span></div>
  </footer>

</main>
</body>
</html>
```